fernbolt website

commerce website to sell cookeries, brackets, mailboxes and to show off homes built. Modern Steel in design see kelvo rides web page to be like: https://www.kelvorides.com/en/ sorry its blue mantis hosting word press divi

must be able to add products to page

Target Market(s)

mainly western states of U.S.

Industry/Entity Type

Building Product

Coding

Coded - Design and coding required

Number of Pages Required

3 page

Font styles to use
Sans Serif

Colors

Designer to choose colors to be used in the design.

Requirements
Must have
• customers to be able to order products from page
• blue mantis hosting word press divi

```html
<!DOCTYPE html>
<html lang="en">
<head>
<meta charset="utf-8">
<title>Fernbolt — About Us</title>
<link rel="stylesheet" href="https://fonts.googleapis.com/css2?family=Poppins:wght@400;500;600&family=Roboto:wght@400;500&display=swap">
<style>
  :root {
    --brand: #43618d;
    --ink: #222222;
    --body: #333333;
    --muted: #555555;
    --paper: #ffffff;
    --band: #f6f6f6;
    --dot: #a9b6c9;
    --photo-light: #9a9c9f;
    --photo-dark: #3c3d40;
  }
  * { box-sizing: border-box; margin: 0; padding: 0; }
  html, body { width: 756px; height: 1200px; overflow: hidden; }
  body { position: relative; background: var(--paper); font-family: "Poppins", sans-serif; color: var(--body); }

  /* Header */
  .site-header { position: absolute; left: 0; top: 0; width: 756px; height: 77px; background: var(--brand); color: #fff; font-family: "Roboto", sans-serif; }
  .brand { position: absolute; left: 55px; top: 28px; display: flex; align-items: center; gap: 6px; font-family: "Poppins", sans-serif; font-weight: 500; font-size: 15px; letter-spacing: .5px; color: #fff; }
  .brand-dot { width: 12px; height: 12px; border-radius: 50%; background: #fff; }
  .main-nav { position: absolute; left: 210px; top: 13px; display: flex; gap: 16.5px; font-size: 8.4px; }
  .promo-links { position: absolute; right: 56px; top: 14px; font-size: 7.6px; }
  .search { position: absolute; left: 211px; top: 37px; width: 272px; height: 23px; display: flex; background: #fff; }
  .search-scope { width: 28px; font-size: 6.5px; font-weight: 500; color: #555; display: flex; align-items: center; justify-content: center; border-right: 1px solid #ddd; margin: 5px 0; }
  .search-field { flex: 1; font-size: 6.8px; color: #777; padding-left: 12px; display: flex; align-items: center; }
  .search-btn { width: 31px; background: #6a8fc4; display: flex; align-items: center; justify-content: center; }
  .account-bar { position: absolute; left: 494px; top: 39px; display: flex; gap: 10px; font-size: 7.4px; line-height: 9px; color: #dfe6f1; }
  .account-item { display: flex; align-items: center; gap: 5px; }

  /* Page title bar */
  .page-title { position: absolute; left: 56px; top: 91px; font-size: 11px; font-weight: 500; letter-spacing: .6px; color: var(--ink); }
  .breadcrumb { position: absolute; right: 56px; top: 92px; font-size: 8.6px; color: var(--ink); }

  /* About band */
  .about-band { position: absolute; left: 0; top: 116px; width: 756px; height: 583px; background: var(--band); }
  .hero-mark { position: absolute; left: 81px; top: 190px; width: 270px; text-align: center; }
  .hero-mark .mark-circle { width: 64px; height: 64px; border-radius: 50%; background: var(--brand); margin: 0 auto 14px; }
  .hero-mark .mark-name { font-size: 40px; font-weight: 500; color: var(--brand); letter-spacing: 1px; line-height: 1; }
  .eyebrow { position: absolute; left: 396px; top: 182px; font-size: 13.4px; font-weight: 500; color: var(--brand); letter-spacing: .4px; }
  .headline { font-weight: 600; color: var(--ink); letter-spacing: .4px; }
  .welcome-title { position: absolute; left: 396px; top: 195px; font-size: 28px; }
  .copy { font-size: 9.6px; line-height: 15.1px; color: var(--body); }
  .copy p + p { margin-top: 7px; }
  .welcome-copy { position: absolute; left: 399px; top: 233px; width: 302px; }
  .commit-title { position: absolute; left: 56px; top: 453px; font-size: 24.5px; line-height: 26.5px; }
  .commit-copy { position: absolute; left: 58px; top: 511px; width: 302px; }
  .cookware-photo { position: absolute; left: 390px; top: 418px; width: 308px; height: 205px; background: linear-gradient(160deg, var(--photo-light), var(--photo-dark)); }

  /* Testimonials */
  .section-title { position: absolute; left: 0; width: 756px; text-align: center; top: 744px; font-size: 19px; }
  .avatar { position: absolute; left: 350px; top: 776px; width: 56px; height: 56px; border-radius: 50%; background: linear-gradient(160deg, #c9c9c9, #8a817c); }
  .quote { position: absolute; left: 178px; top: 840px; width: 400px; text-align: center; font-size: 10px; line-height: 15.2px; color: var(--muted); }
  .quote-name { position: absolute; left: 0; width: 756px; text-align: center; top: 894px; font-size: 8px; font-weight: 500; color: var(--brand); font-family: "Roboto", sans-serif; letter-spacing: .3px; }
  .dots { position: absolute; left: 366px; top: 912px; display: flex; gap: 3px; }
  .dots span { width: 6px; height: 6px; border-radius: 50%; background: var(--dot); }
  .dots span.active { background: var(--brand); }

  /* Footer */
  .site-footer { position: absolute; left: 0; top: 966px; width: 756px; height: 234px; background: var(--brand); color: #fff; font-family: "Roboto", sans-serif; }
  .footer-brand { position: absolute; left: 56px; top: 52px; width: 150px; text-align: center; }
  .footer-brand .mark-circle { width: 34px; height: 34px; border-radius: 50%; background: #fff; margin: 0 auto 8px; }
  .footer-brand .mark-name { font-family: "Poppins", sans-serif; font-size: 20px; font-weight: 500; letter-spacing: .6px; }
  .footer-brand .tagline { margin-top: 10px; font-size: 7.7px; line-height: 11.5px; }
  .footer-col { position: absolute; top: 58px; }
  .footer-col h3 { font-size: 9.6px; font-weight: 500; letter-spacing: .2px; margin-bottom: 6px; }
  .footer-col ul { list-style: none; padding-left: 2px; font-size: 9px; line-height: 15.7px; }
  .col-info { left: 258px; } .col-links { left: 390px; } .col-contact { left: 533px; }
  .contact-list { list-style: none; font-size: 8.2px; line-height: 11.5px; }
  .contact-list li { display: flex; gap: 5px; margin-bottom: 4px; }
  .contact-list svg { flex: none; margin-top: 2px; }
  .social { display: flex; gap: 9px; margin-top: 8px; }
  .social span { width: 7px; height: 7px; border-radius: 50%; background: #fff; }
  .footer-rule { position: absolute; left: 56px; top: 199px; width: 644px; height: 1px; background: rgba(255,255,255,.18); }
  .copyright { position: absolute; left: 56px; top: 213px; font-size: 8.3px; font-weight: 500; }
  .legal { position: absolute; right: 56px; top: 213px; font-size: 8.3px; font-weight: 500; }
  .to-top { position: absolute; left: 716px; top: 188px; width: 22px; height: 22px; border-radius: 50%; background: #fff; display: flex; align-items: center; justify-content: center; }
</style>
</head>
<body>

<header class="site-header">
  <div class="brand"><span class="brand-dot"></span>FERNBOLT</div>
  <nav class="main-nav"><span>Today's Deals</span><span>Help</span><span>Registry</span><span>Gift Cards</span><span>Sell</span></nav>
  <div class="promo-links">One Request, Multiple Quotes &nbsp;|&nbsp; Shop Today's Deals</div>
  <div class="search">
    <div class="search-scope">ALL</div>
    <div class="search-field">Search for Products, Brands and More</div>
    <div class="search-btn"><svg width="9" height="9" viewBox="0 0 10 10"><circle cx="4" cy="4" r="3" fill="none" stroke="#fff" stroke-width="1.2"/><line x1="6.3" y1="6.3" x2="9" y2="9" stroke="#fff" stroke-width="1.2"/></svg></div>
  </div>
  <div class="account-bar">
    <div class="account-item"><svg width="16" height="17" viewBox="0 0 16 17"><circle cx="8" cy="5" r="4" fill="none" stroke="#fff" stroke-width="1.2"/><path d="M1 16c0-4 3-6 7-6s7 2 7 6" fill="none" stroke="#fff" stroke-width="1.2"/></svg><div>Sign In Join Free<br>Fernbolt</div></div>
    <div class="account-item"><svg width="15" height="18" viewBox="0 0 15 18"><rect x="1" y="5" width="13" height="12" fill="none" stroke="#fff" stroke-width="1.2"/><path d="M4.5 7V4a3 3 0 0 1 6 0v3" fill="none" stroke="#fff" stroke-width="1.2"/></svg><div>Order<br>Protection</div></div>
    <div class="account-item"><svg width="19" height="17" viewBox="0 0 19 17"><path d="M9.5 16 2 8.5A4.3 4.3 0 0 1 9.5 3a4.3 4.3 0 0 1 7.5 5.5Z" fill="none" stroke="#fff" stroke-width="1.2"/></svg><div>0<br>Favorites</div></div>
  </div>
</header>

<h1 class="page-title">ABOUT US</h1>
<div class="breadcrumb">Home / About Us</div>

<section class="about-band"></section>
<div class="hero-mark"><div class="mark-circle"></div><div class="mark-name">FERNBOLT</div></div>
<div class="eyebrow">WELCOME TO</div>
<h2 class="headline welcome-title">FERNBOLT</h2>
<div class="copy welcome-copy">
  <p>Lorem Ipsum is simply dummy text of the printing and typesetting industry. Lorem Ipsum has been the industry's standard dummy text ever since the 1500s, when an unknown printer took a galley of type and scrambled it to make a type specimen book. It has survived not only five centuries.</p>
  <p>Lorem Ipsum is simply dummy text of the printing and typesetting industry. Lorem Ipsum has been the industry's standard dummy text ever since ,</p>
</div>
<h2 class="headline commit-title">COMMITTED TO A<br>SUSTAINABLE FUTURE</h2>
<div class="copy commit-copy"><p>Lorem Ipsum is simply dummy text of the printing and typesetting industry. Lorem Ipsum has been the industry's standard dummy text ever since the 1500s, when an unknown printer took a galley of type and scrambled it to make a type specimen book. It has survived not only five centuries.</p></div>
<div class="cookware-photo" role="img" aria-label="Product photo: cooking pot with glass lid on a ceramic cooktop"></div>

<h2 class="headline section-title">TESTIMONIALS</h2>
<div class="avatar" role="img" aria-label="Portrait photo of the customer"></div>
<p class="quote">Lorem Ipsum is simply dummy text of the printing and typesetting industry. Lorem Ipsum has been the industry's standard dummy text ever since thewhen an unknown printer took a galley of type and scrambled .</p>
<div class="quote-name">DANA WHITLOW</div>
<div class="dots"><span class="active"></span><span></span><span></span></div>

<footer class="site-footer">
  <div class="footer-brand">
    <div class="mark-circle"></div>
    <div class="mark-name">FERNBOLT</div>
    <p class="tagline">Lorem ipsum dolor sit amet, consectetur adipisicing elit, sed do eiusmod .</p>
  </div>
  <div class="footer-col col-info"><h3>INFORMATION</h3><ul><li>My Account</li><li>Wishlist</li><li>About Us</li><li>Contact Us</li><li>Blog</li></ul></div>
  <div class="footer-col col-links"><h3>QUICK LINKS</h3><ul><li>Shipping policy</li><li>Size Chart</li><li>Login</li><li>My Account</li><li>Register</li></ul></div>
  <div class="footer-col col-contact"><h3>CONTACT US</h3>
    <ul class="contact-list">
      <li><svg width="6" height="8" viewBox="0 0 6 8"><path d="M3 8C1 5 0 4 0 3a3 3 0 0 1 6 0c0 1-1 2-3 5Z" fill="#fff"/><circle cx="3" cy="3" r="1" fill="var(--brand)"/></svg><span>Your current address goes to here,120<br>example, country.</span></li>
      <li><svg width="7" height="7" viewBox="0 0 7 7"><path d="M1 0l1.5 1.8-1 1a4 4 0 0 0 2.7 2.7l1-1L7 6 6 7C3 7 0 4 0 1Z" fill="#fff"/></svg><span>(008) 310 442 118 20931</span></li>
      <li><svg width="7" height="6" viewBox="0 0 7 6"><rect width="7" height="6" fill="#fff"/><path d="M0 0l3.5 3L7 0" fill="none" stroke="var(--brand)" stroke-width=".8"/></svg><span>hello@fernbolt.com</span></li>
    </ul>
    <div class="social"><span></span><span></span><span></span><span></span><span></span><span></span></div>
  </div>
  <div class="footer-rule"></div>
  <div class="copyright">© 2020 Fernbolt | All Rights Reserved.</div>
  <div class="legal">PRIVACY POLICY - TERMS OF USE</div>
  <div class="to-top"><svg width="7" height="5" viewBox="0 0 7 5"><path d="M1 4l2.5-2.5L6 4" fill="none" stroke="#333" stroke-width="1.2"/></svg></div>
</footer>

</body>
</html>
```